Business Card Design for drone videography and photography

I have a Vexor Talon 3 drone. I am looking for a logo to somehow incorporate with my business name. I don't even know what is an appropriate font. I am most filming real estate homes. I want something simplistic and a logo that makes sense for the business that I'm in. xxxxxxxxxxxxxxxxxxxxxxxxxxxxxxxxxxxxxxxxxxxxxxxxxxxxxxxxxxxxxxxxxxxxxxxxxxxxxxxxxxxxxxxxxxxxxxxxxxxxxxxxxxxxxxxxxxxxxxxxxxxxxxxxxxxxxxxxxxxxxxxxxxxxxxxxxxxxxxxxxxxxxxxxxxxxxxxxxxxxxxxxxxxxxxxxxxxxxxxxxxxxxxxxxxxxxxxxxxxxxxxxxxxxxxxxxxxxxxxxxxxxxxxxxxxxxxxxxxxxxxxxxxxxxxxxxxxxxxxxxxxxxxxxxxxxxxxxxxxxxxxxxxxxxxxxxxxxxxxxxxxxxxxxxxxxxxxxxxxxxxxxxxxxxxxxxxxxxxxxxxxxxxxxxxxxxxxxxxxxxxxxxxxxxxxxxxxxxxxxxxxxxxxxxxxxxxxxxxxxxxxxxxxxxxxxxxxxxxxxxxxxxxxxxxxxxxxxxxxxxxxxxxxxxxxxxxxxxxxxxxxxxxxxxxxxxxxxxxxxxxxxxxxxxxxxxxxxxxxxxxxxxxxxxxxxxxxxxxxxxxxxxxxxxxxxxxxxxxxxxxxxxxxxxxxxxxxxxxxxxxxxxxxxxxxxxxxxxxxxxxxxxxxxxxxxxxxxxxxxxxxxxxxxxxxxxxxxxxxxxxxxxxxxxxxxxxxxxxxxxxxxxxxxxxxxxxxxxxxxxxxxxxxxxxxxxxxxxxxxxxxxxxxxxxxxxxxxxxxxxxxxxxxxxxxxxxxxxxxxxxxxxxxxxxxxxxxxxxxxxxxxxxxxxxxxxxxxxxxxxxxxxxxxxxxxxxxxxxxxxxxxxxxxxxxxxxxxxxxxxxxxxxxxxxxxxxxxxxxxxxxxxxxxxxxxxxxxxxxxxxxxxxxxxxxxxxxxxxxxxxxxxxxxxxxxxxxxxxxxxxxxxxxxxxxxxxxxxxxxxxxxxxxxxxxxxxxxxxxxxxxxxxxxxxxxxxxxxxxxxxxxxxxxxxxxxxxxxxxxxxxxxxxxxxxxxxxxxxxxxxxxxxxxxxxxxxxxxxxxxxxxxxxxxxxxxxxxxxxx

Target Market(s)

Real estate

Industry/Entity Type

Business

Contact Information for Business Card

BRANDT SKYVIEW STUDIO
Daniel Brandt
Owner/Operator

48305 Birch Way
Harlow Springs MO 64990

314-720-4163
dbrandt@brandtskyviewstudio.example

NCQ Drone Certified
Insured
Section 333 Exempt
Halvo Wing Class Certified

Font styles to use
Other font styles liked:
• PUMP DEMI BOLD LET

Requirements
Must have
• Maybe have the certifications on the back??? The business card must be more serious than playful
Nice to have
• Possibly have the logo work itself into the business name?
Should not have
• nothing that looks like a "fun" business. I want this business card to look professional but also simplistic. I don't want a picture that I took from my drone as the background.

```html
<!DOCTYPE html>
<html lang="en">
<head>
<meta charset="utf-8">
<title>Brandt Skyview Studio – Business Card</title>
<link rel="stylesheet" href="https://fonts.googleapis.com/css2?family=Source+Sans+3:wght@400;600&display=swap">
<style>
  :root {
    --backdrop: #ebe7e3;
    --card-white: #ffffff;
    --card-ink: #231f20;
    --text-light: #ffffff;
    --text-dark: #231f20;
  }
  * { margin: 0; padding: 0; box-sizing: border-box; }
  html, body { width: 1200px; height: 900px; overflow: hidden; }
  body {
    background: var(--backdrop);
    font-family: "Source Sans 3", "Myriad Pro", Arial, sans-serif;
    position: relative;
  }
  .card {
    position: absolute;
    background: var(--card-white);
    box-shadow: 0 6px 18px rgba(0,0,0,0.18);
    overflow: hidden;
  }
  /* Front card */
  .card-front { left: 77px; top: 34px; width: 589px; height: 363px; }
  .card-front .brand-area {
    position: absolute; left: 0; top: 0; width: 100%; height: 182px;
  }
  .card-front .contact-band {
    position: absolute; left: 0; top: 182px; width: 100%; height: 181px;
    background: var(--card-ink); color: var(--text-light);
    padding: 14px 32px 0;
  }
  .brand {
    position: absolute;
    display: flex; align-items: center; gap: 12px;
    font-weight: 600; letter-spacing: 2px; line-height: 1.05;
  }
  .brand-mark {
    width: 22px; height: 22px; border-radius: 50%;
    border: 5px solid currentColor; flex: none;
  }
  .card-front .brand { left: 32px; top: 58px; color: var(--text-dark); font-size: 30px; }
  .person-name { font-size: 22px; font-weight: 600; line-height: 1.15; }
  .person-role { font-size: 16px; font-weight: 400; margin-bottom: 20px; }
  .contact-line {
    display: flex; align-items: center; gap: 8px;
    font-size: 16px; font-weight: 400; height: 25px;
  }
  .contact-line svg { width: 13px; height: 13px; fill: var(--text-light); flex: none; }
  .contact-address { font-size: 16px; margin-top: 6px; }

  /* Back card */
  .card-back { left: 388px; top: 505px; width: 567px; height: 352px; }
  .card-back .logo-band {
    position: absolute; left: 0; top: 96px; width: 100%; height: 165px;
    background: var(--card-ink);
    display: flex; align-items: center; justify-content: center;
  }
  .card-back .brand { position: static; color: var(--text-light); font-size: 30px; }
</style>
</head>
<body>

  <section class="card card-front" aria-label="Business card front">
    <div class="brand-area">
      <div class="brand">
        <span class="brand-mark" aria-hidden="true"></span>
        <span>BRANDT SKYVIEW<br>STUDIO</span>
      </div>
    </div>
    <div class="contact-band">
      <p class="person-name">Daniel Brandt</p>
      <p class="person-role">Owner/Operator</p>
      <p class="contact-line">
        <svg viewBox="0 0 24 24" aria-hidden="true"><path d="M6.6 10.8a15.1 15.1 0 0 0 6.6 6.6l2.2-2.2c.3-.3.7-.4 1-.2 1.1.4 2.3.6 3.6.6.6 0 1 .4 1 1V20c0 .6-.4 1-1 1A17 17 0 0 1 3 4c0-.6.4-1 1-1h3.5c.6 0 1 .4 1 1 0 1.3.2 2.5.6 3.6.1.3 0 .7-.2 1z"/></svg>
        555-720-4163
      </p>
      <p class="contact-line">
        <svg viewBox="0 0 24 24" aria-hidden="true"><path d="M2 5h20v14H2zm2 2v.5l8 5 8-5V7l-8 5z"/></svg>
        dbrandt@brandtskyviewstudio.example
      </p>
      <p class="contact-address">48305 Birch Way Harlow Springs MO 64990</p>
    </div>
  </section>

  <section class="card card-back" aria-label="Business card back">
    <div class="logo-band">
      <div class="brand">
        <span class="brand-mark" aria-hidden="true"></span>
        <span>BRANDT SKYVIEW<br>STUDIO</span>
      </div>
    </div>
  </section>

</body>
</html>
```